Used Car Dealer seeks an Amazing Business Card Design

We are looking for a business card design that incorporates our logo and grabs the attention of anyone we give the business card to.

Looking to use the same colors as the logo. Our Logo choice is the black background with Red and Silver/Grey Lettering.

We also would like to see some embossed designs.

Target Market(s)

Used Car Buyers, Automotive, Auto

Industry/Entity Type

Automotive

Contact Information for Business Card

BVEL7K
Gordon Whitlock
482 Tarrow Lane
Suite 207
Roswell, GA 30075
Office (770) 555-0142
Cell (770) 555-0187
bvel7kga@quellmail.com
www.bvel7kga.com

Colors
ffffff
ee3036

Requirements
Must have
• Must include our logo (Black Background with Red and Silver/Grey Lettering)
Nice to have
• Embossed Design. Can be Single or Double Sided.

```html
<!DOCTYPE html>
<html lang="en">
<head>
<meta charset="utf-8">
<title>BVEL7K Business Card</title>
<link href="https://fonts.googleapis.com/css2?family=Open+Sans:wght@400;600;700&display=swap" rel="stylesheet">
<style>
  :root {
    --bg: #3a3a3a;
    --card-black: #0c0c0c;
    --card-black-light: #222;
    --brand-red: #ee3036;
    --deep-red: #7a0000;
    --mid-red: #c40a0a;
    --white: #ffffff;
    --text-light: #e9e9e9;
    --silver: #c9c9c9;
  }
  * { margin: 0; padding: 0; box-sizing: border-box; }
  html, body {
    width: 1200px; height: 750px; overflow: hidden;
    background: var(--bg);
    font-family: "Open Sans", sans-serif;
  }
  .stage { position: relative; width: 1200px; height: 750px; }
  .card {
    position: absolute; top: 228px;
    width: 461px; height: 262px;
    border-radius: 14px; overflow: hidden;
    box-shadow: 0 6px 14px rgba(0,0,0,.55);
  }
  .card--front {
    left: 124px;
    background: radial-gradient(ellipse at 45% 40%, var(--card-black-light) 0%, var(--card-black) 70%);
  }
  .card--back {
    left: 618px;
    background: radial-gradient(ellipse at 50% 40%, var(--mid-red) 0%, var(--deep-red) 95%);
  }
  .front-band {
    position: absolute; left: 0; right: 0; bottom: 0; height: 14px;
    background: linear-gradient(to bottom, var(--brand-red), #a80000);
    border-top: 2px solid var(--silver);
  }
  .brand-name {
    position: absolute; font-weight: 700; letter-spacing: 1px;
  }
  .card--front .brand-name {
    left: 48px; top: 100px; font-size: 34px; color: var(--silver);
  }
  .card--back .brand-name {
    left: 0; right: 0; top: 96px; text-align: center;
    font-size: 50px; color: #0a0a0a;
  }
  .divider {
    position: absolute; left: 253px; top: 56px; width: 1px; height: 152px;
    background: linear-gradient(to bottom, transparent, #666 20%, #666 80%, transparent);
  }
  .contact { position: absolute; left: 274px; top: 54px; color: var(--text-light); }
  .contact__name {
    color: var(--brand-red); font-weight: 600; font-size: 16px;
    text-transform: uppercase; margin-bottom: 4px;
  }
  .contact__address { font-size: 12.5px; line-height: 16.5px; margin-bottom: 8px; }
  .contact__list { list-style: none; font-size: 12.5px; line-height: 17.5px; }
  .contact__list li { display: flex; align-items: center; gap: 6px; }
  .contact__list svg { width: 11px; height: 11px; fill: var(--brand-red); flex: none; }
</style>
</head>
<body>
<div class="stage">
  <section class="card card--front">
    <div class="brand-name">BVEL7K</div>
    <div class="divider"></div>
    <div class="contact">
      <p class="contact__name">Gordon Whitlock</p>
      <p class="contact__address">482 Tarrow Lane<br>Suite 207<br>Roswell, GA 30075</p>
      <ul class="contact__list">
        <li><svg viewBox="0 0 12 12"><path d="M2.5 1 4.5 3.2 3.6 4.6c.7 1.5 2 2.8 3.6 3.6L8.6 7.3 11 9.3 9.8 11C5.3 10.6 1.3 6.6 1 2.2Z"/></svg>(770) 555-0142</li>
        <li><svg viewBox="0 0 12 12"><path d="M3.5 0h5a1 1 0 0 1 1 1v10a1 1 0 0 1-1 1h-5a1 1 0 0 1-1-1V1a1 1 0 0 1 1-1Zm.6 1.5v7.5h3.8V1.5Z"/></svg>(770) 555-0187</li>
        <li><svg viewBox="0 0 12 12"><path d="M0 2.5h12v7H0Zm1 .8 5 3.3 5-3.3Z"/></svg>bvel7kga@quellmail.com</li>
        <li><svg viewBox="0 0 12 12"><circle cx="6" cy="6" r="6"/></svg>www.bvel7kga.com</li>
      </ul>
    </div>
    <div class="front-band"></div>
  </section>

  <section class="card card--back">
    <div class="brand-name">BVEL7K</div>
  </section>
</div>
</body>
</html>
```